Design a poster that illustrates the six central pillars of our school district's efforts with students. The attached PDF outlines the six main competencies we aim for students to possess upon graduation. Each of the 6 has 3 bullet points for the poster as well. The title is "Profile of a Kestrel". Our mascot is this attached winged wheel. The overall concept is that staff take kids when they are young and develop these 6 things when they graduate. Our colors are navy, red, and white. We will make this poster in a variety of sizes in offices, classrooms, and in digital spaces as well. On the PDF - ignore the column that says "Synthesis". That has nothing to do with this poster.

The district is Harlow Creek Public Schools https://www.harlowcreek-schools.example/

```html
<!DOCTYPE html>
<html lang="en">
<head>
<meta charset="utf-8">
<title>Profile of a Kestrel – Competency Suggestions</title>
<link href="https://fonts.googleapis.com/css2?family=Oswald:wght@700&family=Hind:wght@500;700&display=swap" rel="stylesheet">
<style>
  :root {
    --navy: #0e1240;
    --red: #9d1d26;
    --white: #ffffff;
    --ink: #111111;
    --rule: #111111;
  }
  * { box-sizing: border-box; margin: 0; padding: 0; }
  html, body { width: 950px; height: 1200px; overflow: hidden; background: var(--white); }
  .poster {
    position: relative;
    width: 950px;
    height: 1200px;
    overflow: hidden;
    background: var(--white);
    font-family: "Hind", Arial, sans-serif;
    color: var(--ink);
  }
  .poster-title {
    position: absolute;
    left: 55px;
    top: 48px;
    font-family: "Oswald", "Arial Narrow", sans-serif;
    font-weight: 700;
    font-size: 56px;
    line-height: 1;
    color: var(--navy);
    text-transform: uppercase;
  }
  .district-mark {
    position: absolute;
    right: 58px;
    top: 62px;
    display: flex;
    align-items: center;
    gap: 10px;
    font-family: "Oswald", "Arial Narrow", sans-serif;
    font-weight: 700;
    font-size: 26px;
    line-height: 1;
    color: var(--navy);
    text-transform: uppercase;
  }
  .district-mark .dot {
    width: 26px; height: 26px; border-radius: 50%;
    background: var(--red);
  }
  .competency-table {
    position: absolute;
    left: 57px;
    top: 132px;
    width: 836px;
    border-collapse: collapse;
    border: 2.5px solid var(--rule);
    table-layout: fixed;
  }
  .col-name { width: 158px; }
  .competency-table th,
  .competency-table td { border: 2px solid var(--rule); vertical-align: top; }
  .table-caption-row th {
    height: 51px;
    vertical-align: middle;
    font-weight: 700;
    font-size: 25px;
    line-height: 1;
    padding-top: 4px;
    color: var(--navy);
    text-transform: uppercase;
  }
  .column-head th {
    height: 46px;
    vertical-align: middle;
    background: var(--red);
    color: var(--white);
    font-weight: 700;
    font-size: 18px;
    line-height: 1;
    padding-top: 4px;
    text-transform: uppercase;
    letter-spacing: 0.4px;
  }
  .column-head .head-competency { text-align: left; padding-left: 13px; }
  .column-head .head-details { text-align: center; }
  .competency-name {
    padding: 18px 0 0 13px;
    font-size: 16.5px;
    font-weight: 500;
    line-height: 22px;
  }
  .detail-list {
    list-style: none;
    padding: 18px 8px 0 18px;
  }
  .detail-list li {
    position: relative;
    padding-left: 26px;
    font-size: 16.5px;
    font-weight: 500;
    line-height: 22px;
    margin-bottom: 13px;
  }
  .detail-list li:last-child { margin-bottom: 0; }
  .detail-list li::before {
    content: "";
    position: absolute;
    left: 0; top: 3px;
    width: 14px; height: 14px;
    border-radius: 50%;
    background: var(--navy);
  }
  .detail-list li::after {
    content: "";
    position: absolute;
    left: 5px; top: 5.5px;
    width: 3px; height: 6px;
    border-right: 2px solid var(--white);
    border-bottom: 2px solid var(--white);
    transform: rotate(45deg);
  }
  .row-communicator td { height: 130px; }
  .row-thinker td { height: 152px; }
  .row-responsible td { height: 133px; }
  .row-adaptable td { height: 157px; }
  .row-collaborator td { height: 132px; }
  .row-compassionate td { height: 153px; }

  .contact-band {
    position: absolute;
    left: 0; bottom: 0;
    width: 950px; height: 82px;
    background: var(--navy);
    color: var(--white);
    display: flex;
    align-items: center;
    justify-content: space-between;
    padding: 0 44px 0 56px;
    font-size: 16px;
    font-weight: 500;
    white-space: nowrap;
  }
  .contact-item { display: flex; align-items: center; gap: 8px; line-height: 1.25; }
  .contact-item svg { width: 22px; height: 22px; flex: none; }
  .contact-address strong { display: block; font-weight: 700; }
</style>
</head>
<body>
<main class="poster">
  <h1 class="poster-title">Profile of a Kestrel</h1>
  <div class="district-mark"><span class="dot"></span>Harlow Creek</div>

  <table class="competency-table">
    <colgroup><col class="col-name"><col class="col-details"></colgroup>
    <thead>
      <tr class="table-caption-row"><th colspan="2">Competency Suggestions</th></tr>
      <tr class="column-head"><th class="head-competency">Competency</th><th class="head-details">Details</th></tr>
    </thead>
    <tbody>
      <tr class="row-communicator">
        <td class="competency-name">Communicator</td>
        <td><ul class="detail-list">
          <li>Expresses ideas clearly and respectfully (written &amp; verbal).</li>
          <li>Listens actively and understands diverse perspectives.</li>
          <li>Adjusts communication to suit the audience and context.</li>
        </ul></td>
      </tr>
      <tr class="row-thinker">
        <td class="competency-name">Critical Thinker</td>
        <td><ul class="detail-list">
          <li>Questions, analyzes, and evaluates information from multiple sources.</li>
          <li>Identifies and solves complex problems creatively.</li>
          <li>Uses evidence and diverse perspectives to form reasoned conclusions and make informed decisions.</li>
        </ul></td>
      </tr>
      <tr class="row-responsible">
        <td class="competency-name">Responsible</td>
        <td><ul class="detail-list">
          <li>Takes ownership of actions, choices, and commitments.</li>
          <li>Manages time, resources, and self to meet expectations.</li>
          <li>Acts with integrity and advocates for self and others.</li>
        </ul></td>
      </tr>
      <tr class="row-adaptable">
        <td class="competency-name">Adaptable</td>
        <td><ul class="detail-list">
          <li>Responds productively to new situations, challenges, and feedback.</li>
          <li>Learns from new experiences &amp; applies prior knowledge in evolving contexts.</li>
          <li>Adjusts behavior and approach to effectively engage with diverse groups and environments.</li>
        </ul></td>
      </tr>
      <tr class="row-collaborator">
        <td class="competency-name">Collaborator</td>
        <td><ul class="detail-list">
          <li>Contributes effectively and cooperatively to shared goals.</li>
          <li>Listens actively and values diverse ideas and perspectives.</li>
          <li>Engages respectfully, compromising and leading when appropriate.</li>
        </ul></td>
      </tr>
      <tr class="row-compassionate">
        <td class="competency-name">Compassionate</td>
        <td><ul class="detail-list">
          <li>Understands &amp; acknowledges others’ feelings, perspectives, &amp; experiences.</li>
          <li>Responds with kindness, patience, and support.</li>
          <li>Seeks to connect with and contribute positively to the well-being of others and the community.</li>
        </ul></td>
      </tr>
    </tbody>
  </table>

  <footer class="contact-band">
    <div class="contact-item contact-address">
      <svg viewBox="0 0 24 24" aria-hidden="true"><circle cx="12" cy="12" r="12" fill="#9d1d26"/><path d="M12 5.5a4 4 0 0 0-4 4c0 3 4 7.5 4 7.5s4-4.5 4-7.5a4 4 0 0 0-4-4z" fill="none" stroke="#fff" stroke-width="1.6"/><circle cx="12" cy="9.5" r="1.4" fill="#fff"/></svg>
      <div><strong>Harlow Creek Public Schools</strong>48 Elm St. Harlow Creek, MI 49000</div>
    </div>
    <div class="contact-item">
      <svg viewBox="0 0 24 24" aria-hidden="true"><circle cx="12" cy="12" r="12" fill="#9d1d26"/><path d="M8.5 6.5l2 2.2-1.2 1.6c.8 1.7 2 2.9 3.6 3.7l1.6-1.2 2.2 2-1.2 1.8c-4.3-.6-7.6-3.9-8.3-8.2z" fill="#fff"/></svg>
      <span>555-014-2270</span>
    </div>
    <div class="contact-item">
      <svg viewBox="0 0 24 24" aria-hidden="true"><circle cx="12" cy="12" r="12" fill="#9d1d26"/><rect x="8.5" y="6" width="7" height="4" fill="#fff"/><rect x="6.5" y="10" width="11" height="5" rx="1" fill="#fff"/><rect x="8.5" y="14" width="7" height="4" fill="#fff" stroke="#9d1d26" stroke-width="1"/></svg>
      <span>555-014-2275</span>
    </div>
    <div class="contact-item">
      <svg viewBox="0 0 24 24" aria-hidden="true"><circle cx="12" cy="12" r="12" fill="#9d1d26"/><g fill="none" stroke="#fff" stroke-width="1.3"><circle cx="12" cy="12" r="6.5"/><ellipse cx="12" cy="12" rx="2.8" ry="6.5"/><path d="M5.5 12h13M6.5 9h11M6.5 15h11"/></g></svg>
      <span>harlowcreek-schools.example</span>
    </div>
  </footer>
</main>
</body>
</html>
```